Book Cover design for book about character and ethics

This is an exciting book about what it means to live an authentic life. It revolves around finding a sense of contentment, solid friendships and being a good person. The idea is to move away from chasing excessive wealth, good looks and popularity in order to find happiness. Authentic happiness requires a different chase. This book is also about a solid foundation, priorities and work / life balance.

I want a cover that is CREATIVE and POPS. It needs to stand out on the shelf from other books.

Target Market(s)

High school, college and working professionals.

Font styles to use
Serif

Requirements
Must have
• Title: True Otters: Seek A Grounded Path
• Author Name: Dana Velmoravi
• Creativity - makes the point without being entirely obvious
• Cover must pop in comparison to other books
• Use bright colors
• Easy to read text
• Cool picture or vector art
Nice to have
• Topics to think about:
• 1. Stand out from the crowd
• 2. The world is lying to you about what makes you happy
• 3. Renewal
• 4. Rebuild
• 5. Chase What Matters
• 6. Pushing against the wind
• I included some pics below as guidance
Should not have
• Cannot be cheesy
• Do not put a rabbit on the cover even though the book is called "True Otters"

```html
<!DOCTYPE html>
<html lang="en">
<head>
<meta charset="utf-8">
<title>True Otters: Seek A Grounded Path — Book Cover</title>
<link rel="stylesheet" href="https://fonts.googleapis.com/css2?family=Merriweather:wght@900&family=Open+Sans:ital,wght@1,400&family=Zilla+Slab:wght@300;700&display=swap">
<style>
  :root {
    --teal: #2aa6c7;
    --teal-deep: #1b86a6;
    --teal-light: #4dbfdb;
    --title-yellow: #f5ee3c;
    --dot-yellow: #e8e25a;
    --white: #ffffff;
    --band-black: #111111;
    --emblem-dark: #1a1a1a;
    --emblem-red: #e9494b;
  }
  html, body {
    margin: 0;
    padding: 0;
    width: 789px;
    height: 1200px;
    overflow: hidden;
    background: var(--teal);
  }
  .cover {
    position: relative;
    width: 789px;
    height: 1200px;
    overflow: hidden;
  }
  .paper-texture {
    position: absolute;
    inset: 0;
    background:
      radial-gradient(ellipse at 30% 20%, var(--teal-light) 0%, transparent 55%),
      radial-gradient(ellipse at 75% 80%, var(--teal-deep) 0%, transparent 60%),
      var(--teal);
  }
  .title-block {
    position: absolute;
    left: 0;
    top: 0;
    width: 789px;
    height: 520px;
  }
  .title-text {
    font-family: "Merriweather", Georgia, serif;
    font-weight: 900;
    fill: var(--title-yellow);
  }
  .subtitle-text {
    font-family: "Open Sans", Arial, sans-serif;
    font-style: italic;
    font-weight: 400;
    font-size: 58px;
    fill: var(--white);
  }
  .divider {
    stroke: var(--dot-yellow);
    stroke-width: 4;
    stroke-linecap: round;
    stroke-dasharray: 0 10;
  }
  .emblem-area {
    position: absolute;
    left: 212px;
    top: 548px;
    width: 380px;
    height: 384px;
    border-radius: 50%;
    background: radial-gradient(circle at 50% 48%, var(--emblem-red) 0%, var(--emblem-red) 22%, var(--emblem-dark) 52%, var(--emblem-dark) 100%);
  }
  .author-band {
    position: absolute;
    left: 0;
    top: 1052px;
    width: 100%;
    height: 76px;
    background: var(--band-black);
    display: flex;
    align-items: center;
    justify-content: center;
    font-family: "Zilla Slab", Georgia, serif;
    font-size: 45px;
    color: var(--white);
  }
  .author-band .byline { font-weight: 300; margin-right: 12px; }
  .author-band .author-name { font-weight: 700; }
</style>
</head>
<body>
<div class="cover">
  <div class="paper-texture" role="img" aria-label="Crumpled bright teal paper texture background"></div>

  <svg class="title-block" viewBox="0 0 789 520">
    <title>True Otters: Seek A Grounded Path</title>
    <text class="title-text" x="88" y="272" font-size="262" textLength="620" lengthAdjust="spacingAndGlyphs">TRUE</text>
    <text class="title-text" x="84" y="400" font-size="140" textLength="624" lengthAdjust="spacingAndGlyphs">OTTERS</text>
    <line class="divider" x1="198" y1="432" x2="596" y2="432"/>
    <text class="subtitle-text" x="394.5" y="488" text-anchor="middle">Seek A Grounded Path</text>
  </svg>

  <div class="emblem-area" role="img" aria-label="Central emblem: a red heart set in a dark round disc"></div>

  <div class="author-band">
    <span class="byline">Written by</span>
    <span class="author-name">Dana Velmoravi</span>
  </div>
</div>
</body>
</html>
```